Professional Consulting Firm Business Card Design

We need a business card design for a new professional consulting firm that specializes in petroleum, health, and financial consulting. We need a design that is trendy but elegant, and one that would make a vantage 300 executive feel comfortable using our services. I have attached a logo that needs to be used in the design. I have also attached a photo of a card design that I like.

On the card we need a place for employee name, title, email address, fax number, phone number, mailing address, and website address.

Industry/Entity Type

Financial

Contact Information for Business Card

see attached

Font styles to use
Other font styles liked:
• Calibri or your choice

Requirements
Must have
• style
Nice to have
• texture, rounded edges
Should not have
• no solid black cards but black may be used

```html
<!DOCTYPE html>
<html lang="en">
<head>
<meta charset="utf-8">
<title>Northward Advisory – Business Card</title>
<link href="https://fonts.googleapis.com/css2?family=Carlito:wght@400;700&display=swap" rel="stylesheet">
<style>
  :root {
    --backdrop: #d9d6d0;
    --paper: #ebe9e4;
    --paper-speck: rgba(90, 85, 75, 0.10);
    --ink: #2a2b2e;
    --navy: #1e3a70;
    --rule: #2f3033;
  }
  * { box-sizing: border-box; margin: 0; padding: 0; }
  html, body {
    width: 1200px; height: 900px; overflow: hidden;
    background: var(--backdrop);
    font-family: "Carlito", "Calibri", sans-serif;
  }
  .card {
    position: absolute; left: 110px; top: 170px;
    width: 980px; height: 560px;
    border-radius: 10px;
    background-color: var(--paper);
    background-image:
      radial-gradient(var(--paper-speck) 1px, transparent 1.4px),
      radial-gradient(var(--paper-speck) 1px, transparent 1.4px);
    background-size: 17px 19px, 23px 13px;
    background-position: 0 0, 7px 5px;
    box-shadow: 0 14px 30px rgba(0,0,0,0.18);
    color: var(--ink);
  }
  .rule { position: absolute; background: var(--rule); }
  .rule--top { left: 92px; top: 0; width: 3px; height: 118px; }
  .rule--side { right: 0; top: 222px; width: 80px; height: 3px; }
  .rule--bottom { left: 38px; bottom: 0; width: 3px; height: 80px; }

  .brand {
    position: absolute; left: 480px; top: 120px;
    display: flex; align-items: center; gap: 16px;
  }
  .brand__mark { width: 22px; height: 22px; background: var(--navy); }
  .brand__name {
    font-size: 46px; font-weight: 400; letter-spacing: 1px;
    color: var(--navy);
  }

  .person { position: absolute; left: 80px; top: 218px; }
  .person__name { font-size: 34px; font-weight: 700; }
  .person__title { font-size: 20px; font-weight: 700; color: var(--navy); margin-top: 2px; }

  .contacts {
    position: absolute; left: 84px; top: 330px;
    list-style: none; font-size: 25px; line-height: 1;
  }
  .contacts li { display: flex; align-items: center; gap: 14px; margin-bottom: 12px; }
  .contacts .pair { display: flex; align-items: center; gap: 14px; }
  .contacts .pair + .pair { margin-left: 24px; }
  .icon { width: 24px; height: 24px; flex: none; }
</style>
</head>
<body>
  <div class="card">
    <span class="rule rule--top"></span>
    <span class="rule rule--side"></span>
    <span class="rule rule--bottom"></span>

    <div class="brand">
      <span class="brand__mark"></span>
      <span class="brand__name">Northward Advisory</span>
    </div>

    <div class="person">
      <p class="person__name">Your Name</p>
      <p class="person__title">Title</p>
    </div>

    <ul class="contacts">
      <li>
        <svg class="icon" viewBox="0 0 24 24" aria-hidden="true"><rect width="24" height="24" rx="3" fill="#1e3a70"/><path d="M12 5a5 5 0 0 0-5 5c0 4 5 9 5 9s5-5 5-9a5 5 0 0 0-5-5zm0 7a2 2 0 1 1 0-4 2 2 0 0 1 0 4z" fill="#fff"/></svg>
        <span>Headquarters: 1800 North, Harbor Avenue, Lakeview IL</span>
      </li>
      <li>
        <span class="pair">
          <svg class="icon" viewBox="0 0 24 24" aria-hidden="true"><rect width="24" height="24" rx="3" fill="#1e3a70"/><path d="M8 5l2.5 3-1.5 2a9 9 0 0 0 5 5l2-1.5 3 2.5-1.5 2.5C11 18 6 13 5.5 6.5z" fill="#fff"/></svg>
          <span>(555)-014-2200</span>
        </span>
        <span class="pair">
          <svg class="icon" viewBox="0 0 24 24" aria-hidden="true"><rect width="24" height="24" rx="3" fill="#1e3a70"/><rect x="6" y="9" width="12" height="9" fill="#fff"/><rect x="8" y="5" width="8" height="5" fill="#fff"/><rect x="8" y="12" width="8" height="1.5" fill="#1e3a70"/></svg>
          <span>(555)-014-2200</span>
        </span>
      </li>
      <li>
        <svg class="icon" viewBox="0 0 24 24" aria-hidden="true"><rect width="24" height="24" rx="3" fill="#1e3a70"/><rect x="5" y="7" width="14" height="10" fill="#fff"/><path d="M5 7l7 6 7-6" fill="none" stroke="#1e3a70" stroke-width="1.5"/></svg>
        <span>info@northwardadvisory.com</span>
      </li>
      <li>
        <svg class="icon" viewBox="0 0 24 24" aria-hidden="true"><rect width="24" height="24" rx="3" fill="#1e3a70"/><circle cx="12" cy="12" r="6.5" fill="none" stroke="#fff" stroke-width="1.5"/><ellipse cx="12" cy="12" rx="2.8" ry="6.5" fill="none" stroke="#fff" stroke-width="1.3"/><path d="M5.5 12h13" stroke="#fff" stroke-width="1.3"/></svg>
        <span>www.northwardadvisory.com</span>
      </li>
    </ul>
  </div>
</body>
</html>
```